KORVa: AI driven decarbonization application

We are seeking an engaging, user-friendly, and visually appealing user interface for our B2B SaaS platform, Brelmont KORVa. This solution helps large organizations achieve net-zero emissions using AI-driven forecasting, AI models, a emission mitigation library, and a scenario simulator..

A big challenge is to allow the user to work efficiently with multidimensional data.

Requirements:

* Design a modern, professional, and visually striking user interface, catering to a diverse audience within large corporations, including executives, strategists, and environmental specialists.

* Construct an intuitive navigation system, allowing users to seamlessly access functionalities for informed decision-making and tracking progress towards net-zero emissions.

* The application is expected to be used on desktops first

* Incorporate our brand's colors, and visual elements into the design to maintain consistency throughout the application.

* Provide design assets and documentation, such as style guides, design specifications, and necessary assets (e.g., icons, illustrations) for our development team to implement the design. We use Figma and would appreciate delivery as figma files.

Please note that we also need more pages over time. The most important is to get the work bench page right. We will also need:
* a landing page where the users can select previous scenarios and see some high level data.
* A page with information on historical data per asset
* An analytics page
* User and system administration pages.
These pages are out of scope for this project, but they should be available in the navigation solution.

Please submit your initial design concepts, accompanied by a brief explanation of your approach and the rationale behind your design choices. We will offer feedback and collaborate with the chosen designer to refine the design, ensuring it meets our requirements and vision.

We are really hoping to see some elegant user interfaces. The functionality describe in the attachment is important, but the layout is not. Feel free to invent.

Attached files:

Target Market(s)

Energy intensive industries

Requirements
Must have
• Easy to navigate through the different data dimensions: Time, assets, mitigation measures, and advanced details under mitigation measures. The design in the attached files are just our working drafts. Creative alternatives are very welcome.
Nice to have
• Elegant layouts that differ from our working drafts.

```html
<!DOCTYPE html>
<html lang="en">
<head>
<meta charset="utf-8">
<title>Brelmont KORVa – Workbranch</title>
<link href="https://fonts.googleapis.com/css2?family=Inter:wght@400;500;600;700&display=swap" rel="stylesheet">
<style>
:root{
  --navy:#0f4470;
  --navy-dark:#0d3a62;
  --brand:#1c5a92;
  --ink:#1d2733;
  --muted:#8a96a3;
  --faint:#b7c0c9;
  --line:#e3e8ee;
  --panel:#f8fafc;
  --row-hl:#e6f0fa;
  --green:#1aa36a;
  --grey-dot:#a3acb5;
  --red:#e4616f;
  --yellow:#e0a325;
  --purple:#9a6ab9;
  --teal:#5b9b95;
  --timeline:#eef1f4;
}
*{box-sizing:border-box;margin:0;padding:0}
html,body{width:1200px;height:762px;overflow:hidden;background:#fff}
body{font-family:"Inter",sans-serif;color:var(--ink);position:relative}
.abs{position:absolute}

/* header */
.topbar{left:0;top:0;width:1200px;height:47px;background:var(--navy);display:flex;align-items:center;color:#fff}
.brand{width:299px;height:47px;background:var(--brand);display:flex;align-items:center;justify-content:center;font-size:17px;font-weight:500;letter-spacing:3px}
.nav{display:flex;gap:0;font-size:13.5px}
.nav a{color:#fff;text-decoration:none;position:absolute;top:15px}
.nav .active{font-weight:700}
.nav .dot{position:absolute;right:-6px;top:-2px;width:8px;height:8px;border-radius:50%;background:#e5422e}
.quick{left:888px;top:15px;font-size:13.5px;display:flex;align-items:center;gap:8px}
.user{left:1047px;top:15px;font-size:13.5px;display:flex;align-items:center;gap:8px}
.gear{left:1145px;top:10px;width:27px;height:27px;border-radius:50%;background:#2a5f8d;display:flex;align-items:center;justify-content:center}

/* sidebar */
.sidebar{left:0;top:47px;width:299px;height:715px;background:#fff}
.lib-title{left:24px;top:12px;font-size:13px;font-weight:700;color:var(--navy)}
.collapse{left:270px;top:13px}
.search{left:42px;top:44px;width:193px;height:32px;border-radius:8px;background:#eef3f8;display:flex;align-items:center;gap:12px;padding-left:15px;font-size:13.5px;color:#7b8794}
.filter{left:241px;top:43px;width:34px;height:34px;border-radius:50%;background:#e6ecf2;display:flex;align-items:center;justify-content:center}
.groups{left:0;top:95px;width:299px}
.group-head{height:31px;background:var(--navy);color:#fff;display:flex;align-items:center;padding:0 28px 0 27px;font-size:12.2px;margin-bottom:3px}
.group-head .name{flex:1}
.group-head .count{font-size:10.5px;color:#cfe0f0;margin-right:12px}
.items{margin-top:-3px;margin-bottom:3px}
.item{height:27.5px;display:flex;align-items:center;padding:0 50px 0 40px;font-size:12px;color:#6d7884}
.item .name{flex:1}
.item .num{font-size:10.5px;color:var(--faint);margin-right:12px}
.item .box{width:9px;height:9px;border-radius:2px;background:#d4dbe2;position:relative}
.item .box::after{content:"";position:absolute;left:2px;right:2px;top:4px;height:1px;background:#fff}
.item.on{background:var(--row-hl);color:var(--ink)}
.item.on .num{color:var(--navy)}
.item.on .box{background:var(--navy)}

/* assets */
.assets{left:299px;top:47px;width:410px;height:495px;background:var(--panel)}
.panel-title{font-size:13px;font-weight:700;color:var(--navy)}
.asset-table{left:27px;top:45px;width:380px;font-size:10px}
.asset-row{height:26.7px;display:flex;align-items:center}
.asset-row span:nth-child(1){width:104px}
.asset-row span:nth-child(2){width:69px}
.asset-row span:nth-child(3){width:100px}
.asset-row span:nth-child(4){width:77px}
.chk{width:11px;height:11px;border-radius:50%;display:inline-flex;align-items:center;justify-content:center}
.chk.ok{background:var(--green)}
.chk.off{background:var(--grey-dot)}
.adv-bar{left:0;top:264px;width:410px;height:30px;background:#e5e9ee;display:flex;align-items:center;padding:0 28px 0 27px;font-size:10.5px;font-weight:600;color:var(--navy)}
.adv-bar span{flex:1}
.adv-list{left:27px;top:294px;width:355px;font-size:10px}
.adv-row{height:27.5px;display:flex;align-items:center;color:var(--ink)}
.adv-row .label{flex:1}
.adv-row .state{margin-right:9px;color:var(--green)}
.adv-row.inactive .label,.adv-row.inactive .state{color:var(--muted)}

/* simulation */
.sim{left:709px;top:47px;width:491px;height:495px;background:#fff}
.sim-icons{left:375px;top:12px;display:flex;gap:10px}
.sim-icons div{width:27px;height:27px;border-radius:50%;background:#edf1f5;display:flex;align-items:center;justify-content:center}
.sim-icons div.sel{background:var(--navy)}
.legend{left:64px;top:62px;display:flex;gap:22px;font-size:10.5px;color:var(--navy)}
.legend span::before{content:"";display:inline-block;width:7px;height:7px;border-radius:50%;margin-right:6px;background:var(--c)}
.chart{left:0;top:0}

/* timeline */
.timeline{left:299px;top:542px;width:901px;height:220px;background:var(--timeline)}
.tl-svg{left:0;top:0}
.bar{position:absolute;height:31px;display:flex;align-items:center;padding:0 12px 0 10px;color:#fff;font-size:12px}
.bar .name{flex:1}
.bar .mod{font-size:10.5px;margin-right:10px}
.bar .ic{width:11px;height:9px;border-radius:2px;background:#fff;position:relative}
.bar .ic::after{content:"";position:absolute;left:4px;top:3px;width:3px;height:3px;border-radius:50%;background:var(--bc)}
.view-toggle{left:620px;top:170px;width:262px;height:29px;border-radius:15px;background:#fff;display:flex;overflow:hidden;font-size:10.5px;box-shadow:0 1px 3px rgba(0,0,0,.06)}
.view-toggle div{flex:1;display:flex;align-items:center;justify-content:center;gap:9px;color:var(--navy);letter-spacing:.5px}
.view-toggle .cur{background:var(--navy);color:#fff;border-radius:15px 15px 15px 0}
</style>
</head>
<body>

<header class="topbar abs">
  <div class="brand">Brelmont</div>
  <nav class="nav">
    <a style="left:320px">Home</a>
    <a style="left:384px">Assets</a>
    <a style="left:453px" class="active">Workbranch</a>
    <a style="left:561px">Simulation<i class="dot"></i></a>
    <a style="left:653px">Map</a>
  </nav>
  <div class="quick abs">Quick Actions
    <svg width="12" height="16" viewBox="0 0 12 16"><path d="M7 1 2 9h4l-1 6 5-8H6z" fill="none" stroke="#fff" stroke-width="1.3" stroke-linejoin="round"/></svg>
  </div>
  <div class="user abs">John Doe
    <svg width="10" height="6"><path d="M0 0h10L5 6z" fill="#fff"/></svg>
  </div>
  <div class="gear abs">
    <svg width="15" height="15" viewBox="0 0 16 16"><circle cx="8" cy="8" r="2.4" fill="none" stroke="#fff" stroke-width="1.3"/><path d="M8 1.5l1.2 1.6 2-.4.5 2 1.8 1-.8 1.8.8 1.8-1.8 1-.5 2-2-.4L8 14.5l-1.2-1.6-2 .4-.5-2-1.8-1 .8-1.8-.8-1.8 1.8-1 .5-2 2 .4z" fill="none" stroke="#fff" stroke-width="1.2" stroke-linejoin="round"/></svg>
  </div>
</header>

<aside class="sidebar abs">
  <div class="lib-title abs">MEASURES LIBRARY</div>
  <svg class="collapse abs" width="16" height="16" viewBox="0 0 16 16"><rect x="1" y="1" width="14" height="14" fill="none" stroke="var(--navy)" stroke-width="1.6"/><rect x="1" y="1" width="5" height="14" fill="var(--navy)"/><path d="M11 5 8 8l3 3" fill="none" stroke="var(--navy)" stroke-width="1.4"/></svg>
  <div class="search abs">
    <svg width="16" height="16" viewBox="0 0 16 16"><circle cx="6.5" cy="6.5" r="5" fill="none" stroke="#7086a0" stroke-width="1.6"/><path d="m10.5 10.5 4 4" stroke="#7086a0" stroke-width="1.8"/></svg>
    Search measures
  </div>
  <div class="filter abs"><svg width="14" height="14" viewBox="0 0 14 14"><path d="M0 1h14L8.5 7.5V13L5.5 11.5v-4z" fill="#8797a8"/></svg></div>

  <div class="groups abs">
    <div class="group-head"><span class="name">Switch Energy Carrier</span><span class="count">1 Applied</span><svg width="10" height="6"><path d="M0 0h10L5 6z" fill="#fff"/></svg></div>
    <div class="items">
      <div class="item"><span class="name">Ammonium</span><span class="num">0/0</span><i class="box"></i></div>
      <div class="item on"><span class="name">Biodiesel</span><span class="num">20/28</span><i class="box"></i></div>
      <div class="item"><span class="name">Ethanol</span><span class="num">0/0</span><i class="box"></i></div>
      <div class="item"><span class="name">Hydrogen</span><span class="num">0/0</span><i class="box"></i></div>
      <div class="item"><span class="name">LNG</span><span class="num">0/0</span><i class="box"></i></div>
      <div class="item"><span class="name">Methanol</span><span class="num">0/0</span><i class="box"></i></div>
      <div class="item"><span class="name">Power from offshore wind</span><span class="num">0/0</span><i class="box"></i></div>
      <div class="item"><span class="name">Power from shore</span><span class="num">0/0</span><i class="box"></i></div>
    </div>
    <div class="group-head"><span class="name">Energy efficiency Measures</span><span class="count">2 Applied</span><svg width="10" height="6"><path d="M0 0h10L5 6z" fill="#fff"/></svg></div>
    <div class="items">
      <div class="item"><span class="name">Venting to flare</span><span class="num">0/0</span><i class="box"></i></div>
      <div class="item"><span class="name">reduced water injection</span><span class="num">0/0</span><i class="box"></i></div>
      <div class="item on"><span class="name">Reduced gaz injection</span><span class="num">18/18</span><i class="box"></i></div>
      <div class="item on"><span class="name">Compressor replacement</span><span class="num">7/28</span><i class="box"></i></div>
      <div class="item"><span class="name">Venting to production</span><span class="num">0/0</span><i class="box"></i></div>
      <div class="item"><span class="name">Drilling Improvements</span><span class="num">0/0</span><i class="box"></i></div>
      <div class="item"><span class="name">reduced water injection</span><span class="num">0/0</span><i class="box"></i></div>
    </div>
    <div class="group-head"><span class="name">Logisticts</span><span class="count">0 Applied</span><svg width="6" height="10"><path d="M6 0v10L0 5z" fill="#fff"/></svg></div>
    <div class="group-head"><span class="name">End of pipe measures</span><span class="count">0 Applied</span><svg width="6" height="10"><path d="M6 0v10L0 5z" fill="#fff"/></svg></div>
    <div class="group-head"><span class="name">Carbon offsets</span><span class="count">0 Applied</span><svg width="6" height="10"><path d="M6 0v10L0 5z" fill="#fff"/></svg></div>
    <div class="group-head"><span class="name">Company Structure</span><span class="count">0 Applied</span><svg width="6" height="10"><path d="M6 0v10L0 5z" fill="#fff"/></svg></div>
  </div>
</aside>

<section class="assets abs">
  <h2 class="panel-title abs" style="left:16px;top:12px">ASSETS</h2>
  <div class="asset-table abs">
    <div class="asset-row"><span>Asset name</span><span>data</span><span>additionals</span><span>date</span><i class="chk ok"><svg width="7" height="6"><path d="M1 3l2 2 3-4" fill="none" stroke="#fff" stroke-width="1.3"/></svg></i></div>
    <div class="asset-row"><span>Asset name</span><span>data</span><span>additionals</span><span>date</span><i class="chk off"><svg width="7" height="6"><path d="M1 3l2 2 3-4" fill="none" stroke="#fff" stroke-width="1.3"/></svg></i></div>
    <div class="asset-row"><span>Asset name</span><span>data</span><span>additionals</span><span>date</span><i class="chk off"><svg width="7" height="6"><path d="M1 3l2 2 3-4" fill="none" stroke="#fff" stroke-width="1.3"/></svg></i></div>
    <div class="asset-row"><span>Asset name</span><span>data</span><span>additionals</span><span>date</span><i class="chk ok"><svg width="7" height="6"><path d="M1 3l2 2 3-4" fill="none" stroke="#fff" stroke-width="1.3"/></svg></i></div>
    <div class="asset-row"><span>Asset name</span><span>data</span><span>additionals</span><span>date</span><i class="chk ok"><svg width="7" height="6"><path d="M1 3l2 2 3-4" fill="none" stroke="#fff" stroke-width="1.3"/></svg></i></div>
    <div class="asset-row"><span>Asset name</span><span>data</span><span>additionals</span><span>date</span><i class="chk off"><svg width="7" height="6"><path d="M1 3l2 2 3-4" fill="none" stroke="#fff" stroke-width="1.3"/></svg></i></div>
  </div>
  <div class="adv-bar abs"><span>Advanced Settings</span><svg width="10" height="6"><path d="M0 0h10L5 6z" fill="var(--navy)"/></svg></div>
  <div class="adv-list abs">
    <div class="adv-row"><span class="label">Daily Monitoring</span><span class="state">Active</span><i class="chk ok"><svg width="7" height="6"><path d="M1 3l2 2 3-4" fill="none" stroke="#fff" stroke-width="1.3"/></svg></i></div>
    <div class="adv-row inactive"><span class="label">Compression advaced configuration</span><span class="state">inactive</span><i class="chk off"><svg width="7" height="6"><path d="M1 3l2 2 3-4" fill="none" stroke="#fff" stroke-width="1.3"/></svg></i></div>
    <div class="adv-row inactive"><span class="label">Advanced Recast</span><span class="state">inactive</span><i class="chk off"><svg width="7" height="6"><path d="M1 3l2 2 3-4" fill="none" stroke="#fff" stroke-width="1.3"/></svg></i></div>
    <div class="adv-row inactive"><span class="label">Compressor failure safty</span><span class="state">inactive</span><i class="chk off"><svg width="7" height="6"><path d="M1 3l2 2 3-4" fill="none" stroke="#fff" stroke-width="1.3"/></svg></i></div>
    <div class="adv-row"><span class="label">Activated advanced setting</span><span class="state">Active</span><i class="chk ok"><svg width="7" height="6"><path d="M1 3l2 2 3-4" fill="none" stroke="#fff" stroke-width="1.3"/></svg></i></div>
    <div class="adv-row inactive"><span class="label">This is an inactive one</span><span class="state">inactive</span><i class="chk off"><svg width="7" height="6"><path d="M1 3l2 2 3-4" fill="none" stroke="#fff" stroke-width="1.3"/></svg></i></div>
  </div>
</section>

<section class="sim abs">
  <svg class="chart abs" width="491" height="495" viewBox="709 47 491 495" font-family="Inter, sans-serif" font-size="9" fill="var(--navy)">
    <rect x="775" y="133" width="392" height="357" fill="#fbfcfd"/>
    <rect x="831" y="133" width="55" height="357" fill="#eef4fb"/>
    <rect x="942" y="133" width="55" height="357" fill="#eef4fb"/>
    <rect x="1053" y="133" width="55" height="357" fill="#eef4fb"/>
    <line x1="766" y1="490" x2="1173" y2="490" stroke="#dfe4ea"/>
    <text x="744" y="144">20</text><text x="744" y="231">15</text><text x="744" y="318">10</text>
    <text x="746" y="405">5</text><text x="746" y="493">0</text>
    <g text-anchor="middle">
      <text x="828" y="509">2022</text><text x="884" y="509">2023</text><text x="941" y="509">2024</text>
      <text x="998" y="509">2025</text><text x="1054" y="509">2026</text><text x="1111" y="509">2027</text><text x="1167" y="509">2027</text>
    </g>
    <g fill="none" stroke-width="2.4" stroke-linecap="round">
      <path d="M775,315 C800,270 820,247 850,247 C890,247 915,240 950,221 C970,212 990,210 1000,215 C1015,222 1020,240 1035,239 C1055,238 1065,210 1083,200 C1100,191 1130,190 1152,192" stroke="var(--red)"/>
      <path d="M775,315 C810,290 840,265 867,265 C895,265 915,310 942,310 C970,310 1000,282 1033,282 C1060,282 1100,285 1152,290" stroke="var(--yellow)"/>
      <path d="M775,315 C805,295 830,275 850,275 C890,275 930,380 975,382 C1010,384 1030,412 1054,414 C1085,416 1100,440 1120,455 C1135,465 1145,467 1158,467" stroke="var(--teal)"/>
      <path d="M775,315 C800,300 815,290 833,290 C865,290 890,364 921,364 C950,364 975,335 1000,333 C1030,330 1040,328 1060,318 C1100,300 1120,268 1152,265" stroke="var(--purple)"/>
    </g>
  </svg>
  <h2 class="panel-title abs" style="left:19px;top:18px">SIMULATION</h2>
  <div class="sim-icons abs">
    <div class="sel"><svg width="14" height="12" viewBox="0 0 14 12"><rect x="1" y="1" width="12" height="10" rx="1" fill="none" stroke="#fff" stroke-width="1.4"/><path d="M1 9l4-4 3 3 5-5" fill="none" stroke="#fff" stroke-width="1.4"/></svg></div>
    <div><svg width="14" height="14" viewBox="0 0 14 14"><path d="M6 1a6 6 0 1 0 6 7H6z" fill="var(--navy)"/><path d="M8 0v6h6A6 6 0 0 0 8 0z" fill="var(--navy)"/></svg></div>
    <div><svg width="12" height="12" viewBox="0 0 12 12"><rect x="1" y="5" width="2.5" height="7" fill="var(--navy)"/><rect x="5" y="1" width="2.5" height="11" fill="var(--navy)"/><rect x="9" y="7" width="2.5" height="5" fill="var(--navy)"/></svg></div>
  </div>
  <div class="legend abs">
    <span style="--c:var(--purple)">Accumulated Effect</span>
    <span style="--c:var(--yellow)">Second Strategy</span>
    <span style="--c:var(--red)">No Measures</span>
    <span style="--c:var(--teal)">Goal</span>
  </div>
</section>

<section class="timeline abs">
  <svg class="tl-svg abs" width="901" height="220" viewBox="299 542 901 220" font-family="Inter, sans-serif" font-size="10.5" fill="var(--navy)" text-anchor="middle">
    <g stroke="#dde2e8">
      <line x1="329" y1="567" x2="329" y2="762"/><line x1="400" y1="567" x2="400" y2="762"/><line x1="470" y1="567" x2="470" y2="762"/>
      <line x1="540" y1="567" x2="540" y2="762"/><line x1="610" y1="567" x2="610" y2="762"/><line x1="679" y1="567" x2="679" y2="762"/>
      <line x1="748" y1="567" x2="748" y2="762"/><line x1="818" y1="567" x2="818" y2="762"/><line x1="888" y1="567" x2="888" y2="762"/>
      <line x1="957" y1="567" x2="957" y2="762"/><line x1="1027" y1="567" x2="1027" y2="762"/><line x1="1097" y1="567" x2="1097" y2="762"/>
      <line x1="1167" y1="567" x2="1167" y2="762"/>
    </g>
    <text x="329" y="561">2022</text><text x="400" y="561">2023</text><text x="470" y="561">2024</text><text x="540" y="561">2025</text>
    <text x="610" y="561">2026</text><text x="679" y="561">2027</text><text x="748" y="561">2027</text><text x="818" y="561">2029</text>
    <text x="888" y="561">2030</text><text x="957" y="561">2031</text><text x="1027" y="561">2032</text><text x="1097" y="561">2033</text>
    <text x="1167" y="561">2034</text>
  </svg>
  <div class="bar" style="left:30px;top:41px;width:317px;background:var(--yellow);--bc:var(--yellow)"><span class="name">Compressor replacement</span><span class="mod">Modify</span><i class="ic"></i></div>
  <div class="bar" style="left:451px;top:41px;width:278px;background:var(--yellow);--bc:var(--yellow)"><span class="name">Compressor replacement</span><span class="mod">Modify</span><i class="ic"></i></div>
  <div class="bar" style="left:102px;top:83px;width:278px;background:var(--purple);--bc:var(--purple);padding-left:20px"><span class="name">Biodiesel Enery Carrier</span><span class="mod">Modify</span><i class="ic"></i></div>
  <div class="bar" style="left:311px;top:125px;width:278px;background:var(--teal);--bc:var(--teal)"><span class="name">Biodiesel Enery Carrier</span><span class="mod">Modify</span><i class="ic"></i></div>
  <div class="view-toggle abs">
    <div>Measures View <svg width="11" height="11" viewBox="0 0 11 11"><path d="M0 0h11v4H7v7H4V7H0z" fill="var(--navy)"/></svg></div>
    <div class="cur">Assets View <svg width="11" height="10" viewBox="0 0 11 10"><rect width="11" height="10" rx="1.5" fill="#fff"/><rect x="2" y="3" width="7" height="1.4" fill="var(--navy)"/></svg></div>
  </div>
</section>

</body>
</html>
```